Private Equity Fund needs a powerpoint template

We need a power point presentation template for our recent founded firm, Corvane Partners, a private equity/investment fund (funded by investors, is a firm that buys, holds and sells companies years after) focused in turnaround cases. The presentation should address corporate and financial subjects in a clean/plain way, but as most straightforward way as possible. This is a commercial pitch/flip presentation, is not a presentation with animations to be presented to a mass of people.

We would like that the designer resume the file that we began building (adapted from other funds/advisors of the market) and establish the following according to our logo:
1) a new set of fonts (size levels and type),
2) colors (tables, headers, lines),
3) space available for content (text boxes, tables, pictures or charts) (note left column space in blank)
4) set, our Excel applications to use as default, the color guide that you have you defined
5) white background

Basically, we need to change the items listed above to the "Example.ppt" file uploaded along with those instructions.

The presentation should:
A) rule how the people in our organization should address our messages (guide with size of tables, font and size, colors)
B) pattern a set of slides that could minimize the time for arranging formats, worrying only about the content
C) allow the person who is building the presentation to have options while addressing the message

Dont get too restricted to what we are giving you (the "Example.ppt" file). You may suggest:
i) logo positioning
ii) with or without any vague space (left column space in blank)
iii) space optmization
iv) shades and colors
v) fonts (careful with the wide ones as it does not optimizes space)

I'm uploading:

Target Market(s)

Banks
Investors
Company owners/founders
Funds

Industry/Entity Type

Financial Service

Font styles to use
Other font styles liked:
• Arial Narrow, Arial, trojan

Colors

Designer to choose colors to be used in the design.

Requirements
Must have
• We would like that the designer resume the file that we began building (adapted from other funds/advisors of the market) and establish the following according to our logo:
• 1) a new set of fonts (size levels and type),
• 2) colors (tables, headers, lines),
• 3) space available for content (text boxes, tables, pictures or charts) (note left column space in blank)
• 4) set, our Excel applications to use as default, the color guide that you have you defined
• 5) white background
Nice to have
• Narrow font type
• Space optimization
• Discrete
Should not have
• Animations
• Font size too big
• colored background

```html
<!DOCTYPE html>
<html lang="en">
<head>
<meta charset="utf-8">
<title>Corvane Partners – Presentation Template Overview</title>
<link rel="stylesheet" href="https://fonts.googleapis.com/css2?family=Roboto+Condensed:wght@300;400;700&display=swap">
<style>
:root{
  --sage:#9aa389;
  --sage-dark:#7c8670;
  --sage-light:#d3d9c7;
  --sage-pale:#e7eadf;
  --mauve:#8e7380;
  --slate:#7b87a3;
  --taupe:#a89b86;
  --clay:#c0855a;
  --ink:#4b5046;
  --grey:#8d8f89;
  --rule:#cfd2c8;
  --paper:#ffffff;
}
*{box-sizing:border-box;margin:0;padding:0}
html,body{width:1200px;height:3271px;overflow:hidden;background:var(--paper)}
body{font-family:'Roboto Condensed',sans-serif;color:var(--ink);position:relative}
.slide{position:absolute;width:384px;height:288px;background:var(--paper);
  box-shadow:0 0 0 1px #dedfdb,0 2px 5px rgba(0,0,0,.14);overflow:hidden}
.pg{position:absolute;top:0;right:10px;width:9px;height:11px;background:#6b6d68;color:#fff;
  font-size:5px;line-height:11px;text-align:center}
.s-title{position:absolute;left:14px;top:12px;font-size:12.5px;font-weight:400;text-transform:uppercase;
  letter-spacing:.2px;color:var(--ink)}
.s-title.mixed{text-transform:none}
.s-sub{position:absolute;left:14px;top:29px;font-size:5.5px;text-transform:uppercase;color:var(--grey);letter-spacing:.3px}
.art{position:absolute;left:14px;top:44px;width:356px;height:200px}
.strap{position:absolute;left:14px;top:252px;font-size:8px;color:var(--ink)}
.brand{position:absolute;right:12px;bottom:7px;font-size:6.5px;color:var(--grey);letter-spacing:.6px;
  text-transform:uppercase;display:flex;align-items:center;gap:3px}
.brand::before{content:"";width:6px;height:6px;background:var(--grey)}
.t{font-family:'Roboto Condensed',sans-serif;font-size:5px;fill:var(--ink)}
.ts{font-family:'Roboto Condensed',sans-serif;font-size:4px;fill:var(--grey)}
.tw{font-family:'Roboto Condensed',sans-serif;font-size:5px;fill:#fff}
.tb{font-family:'Roboto Condensed',sans-serif;font-size:5px;font-weight:700;fill:var(--ink)}
.f-sage{fill:var(--sage)} .f-dark{fill:var(--sage-dark)} .f-light{fill:var(--sage-light)} .f-pale{fill:var(--sage-pale)}
.f-mauve{fill:var(--mauve)} .f-slate{fill:var(--slate)} .f-taupe{fill:var(--taupe)} .f-clay{fill:var(--clay)}
.ln{stroke:var(--rule);stroke-width:.6;fill:none}
.ln-d{stroke:var(--grey);stroke-width:.6;fill:none}
/* cover */
.cover-brand{position:absolute;left:24px;top:40px;font-size:11px;letter-spacing:1px;text-transform:uppercase;
  color:var(--ink);display:flex;align-items:center;gap:5px}
.cover-brand::before{content:"";width:11px;height:11px;background:var(--ink)}
.cover-rule{position:absolute;left:24px;height:1px;background:var(--grey)}
.cover-title{position:absolute;left:24px;top:70px;font-size:11px;text-transform:uppercase;color:var(--ink)}
.cover-sub{position:absolute;left:24px;top:85px;font-size:6px;text-transform:uppercase;color:var(--grey)}
.divider-title{position:absolute;right:16px;top:150px;font-size:11px;text-transform:uppercase;text-align:right}
.divider-sub{position:absolute;right:16px;top:165px;font-size:6px;text-transform:uppercase;color:var(--grey)}
.divider-brand{position:absolute;right:16px;top:64px;font-size:9px;letter-spacing:1px;text-transform:uppercase;
  color:var(--ink);display:flex;align-items:center;gap:4px}
.divider-brand::before{content:"";width:9px;height:9px;background:var(--ink)}
.map-fill{position:absolute;top:20px;width:160px;height:150px;background:var(--sage-light);border-radius:40% 45% 50% 38%}
.signature{position:absolute;left:610px;top:3080px;width:470px;display:flex;align-items:center;gap:18px;color:#3f403c}
.signature .mark{width:80px;height:80px;background:#3f403c;flex:none}
.signature .name{font-size:62px;font-weight:400;letter-spacing:4px;line-height:1;text-transform:uppercase}
.signature .name span{display:block;font-size:24px;letter-spacing:9px;margin-top:6px}
</style>
</head>
<body>

<svg width="0" height="0" style="position:absolute" aria-hidden="true">
  <defs>
    <g id="pie">
      <path class="f-sage" d="M0 0L0 -28A28 28 0 0 1 16.46 22.65Z"/>
      <path class="f-slate" d="M0 0L16.46 22.65A28 28 0 0 1 -22.65 16.46Z"/>
      <path class="f-mauve" d="M0 0L-22.65 16.46A28 28 0 0 1 -22.65 -16.46Z"/>
      <path class="f-taupe" d="M0 0L-22.65 -16.46A28 28 0 0 1 0 -28Z"/>
    </g>
    <g id="bullets">
      <text class="t" x="4" y="0">• Bullet text</text>
      <text class="t" x="4" y="8">• Bullet text</text>
      <text class="t" x="4" y="16">• Bullet text</text>
      <text class="t" x="4" y="24">• Bullet text</text>
    </g>
    <g id="cv">
      <rect class="f-sage" width="100" height="9"/>
      <text class="tw" x="4" y="6.5">Name Surname</text>
      <text class="tb" x="4" y="18">Global Head of Function</text>
      <text class="t" x="4" y="26">Prior experience</text>
      <text class="t" x="8" y="34">• Transaction 1</text>
      <text class="t" x="8" y="41">• Transaction 2</text>
      <text class="t" x="8" y="48">• Transaction 3</text>
    </g>
  </defs>
</svg>

<!-- Row 1 -->
<section class="slide" style="left:12px;top:12px">
  <div class="cover-brand">Corvane Partners</div>
  <div class="cover-rule" style="top:62px;width:100px"></div>
  <h1 class="cover-title">Presentation title goes here</h1>
  <p class="cover-sub">Your subtitle goes here</p>
  <div class="cover-rule" style="top:98px;width:100px"></div>
</section>

<section class="slide" style="left:408px;top:12px">
  <span class="pg">2</span>
  <h2 class="s-title mixed">Contents</h2>
  <svg class="art" viewBox="0 0 356 200">
    <g transform="translate(70,8)">
      <text class="t" x="0" y="6">Section 1</text><text class="ts" x="0" y="13">Enter title</text><line class="ln-d" x1="0" y1="16" x2="210" y2="16"/><text class="t" x="206" y="13">3</text>
      <text class="t" x="0" y="40">Section 2</text><text class="ts" x="0" y="47">Enter title</text><line class="ln-d" x1="0" y1="50" x2="210" y2="50"/><text class="t" x="206" y="47">5</text>
      <text class="t" x="0" y="74">Section 3</text><text class="ts" x="0" y="81">Enter title</text><line class="ln-d" x1="0" y1="84" x2="210" y2="84"/><text class="t" x="206" y="81">7</text>
      <text class="t" x="0" y="108">Section 4</text><text class="ts" x="0" y="115">Enter title</text><line class="ln-d" x1="0" y1="118" x2="210" y2="118"/><text class="t" x="206" y="115">9</text>
      <text class="t" x="0" y="142">Section 5</text><text class="ts" x="0" y="149">Enter title</text><line class="ln-d" x1="0" y1="152" x2="210" y2="152"/><text class="t" x="202" y="149">11</text>
    </g>
  </svg>
  <span class="brand">Corvane Partners</span>
</section>

<section class="slide" style="left:804px;top:12px">
  <span class="pg">3</span>
  <div class="divider-brand">Corvane Partners</div>
  <h2 class="divider-title">Divider page title here</h2>
  <p class="divider-sub">Your subtitle goes here</p>
</section>

<!-- Row 2 -->
<section class="slide" style="left:12px;top:308px">
  <span class="pg">4</span>
  <h2 class="s-title">Color palette</h2>
  <svg class="art" viewBox="0 0 356 200">
    <g transform="translate(10,6)">
      <text class="ts" x="0" y="4">Main colour</text><rect class="f-sage" y="6" width="40" height="9"/>
      <text class="ts" x="0" y="24">Secondary</text><rect class="f-mauve" y="26" width="40" height="9"/>
      <text class="ts" x="0" y="44">Accent</text><rect class="f-slate" y="46" width="40" height="9"/>
      <text class="ts" x="0" y="64">Neutral</text><rect class="f-taupe" y="66" width="40" height="9"/>
      <text class="ts" x="0" y="84">Light</text><rect class="f-light" y="86" width="40" height="9"/>
    </g>
    <g transform="translate(62,6)">
      <rect class="f-dark" y="6" width="40" height="9"/><rect class="f-light" y="26" width="40" height="9"/>
      <rect class="f-slate" y="46" width="40" height="9" opacity=".6"/><rect class="f-mauve" y="66" width="40" height="9" opacity=".6"/>
      <rect class="f-pale" y="86" width="40" height="9"/>
    </g>
    <g transform="translate(114,6)">
      <rect class="f-taupe" y="6" width="40" height="9" opacity=".6"/><rect class="f-sage" y="26" width="40" height="9" opacity=".6"/>
      <rect class="f-clay" y="46" width="40" height="9"/>
      <text class="ts" x="0" y="78">Chart order</text>
    </g>
    <g transform="translate(190,20)">
      <text class="ts" x="0" y="4">Table header</text><rect class="f-sage" y="6" width="30" height="7"/>
      <text class="ts" x="0" y="24">Table row</text><rect class="f-pale" y="26" width="30" height="7"/>
      <text class="ts" x="0" y="44">Lines</text><line class="ln-d" x1="0" y1="50" x2="30" y2="50"/>
      <text class="ts" x="0" y="64">Text</text><rect fill="#4b5046" y="66" width="30" height="7"/>
    </g>
  </svg>
  <span class="brand">Corvane Partners</span>
</section>

<section class="slide" style="left:408px;top:308px">
  <span class="pg">5</span>
  <h2 class="s-title">1. Standard width layout</h2>
  <p class="s-sub">Your subtitle goes here</p>
  <svg class="art" viewBox="0 0 356 200">
    <rect class="f-sage" width="356" height="8"/><text class="tw" x="4" y="6">Chart title</text>
    <g><rect class="f-slate" x="110" y="13" width="5" height="4"/><text class="ts" x="117" y="17">Series 1</text>
      <rect class="f-taupe" x="145" y="13" width="5" height="4"/><text class="ts" x="152" y="17">Series 2</text>
      <rect class="f-mauve" x="180" y="13" width="5" height="4"/><text class="ts" x="187" y="17">Series 3</text>
      <rect class="f-sage" x="215" y="13" width="5" height="4"/><text class="ts" x="222" y="17">Series 4</text></g>
    <line class="ln" x1="20" y1="40" x2="350" y2="40"/><line class="ln" x1="20" y1="80" x2="350" y2="80"/><line class="ln" x1="20" y1="120" x2="350" y2="120"/>
    <line class="ln-d" x1="20" y1="160" x2="350" y2="160"/>
    <g><rect class="f-slate" x="40" y="50" width="10" height="110"/><rect class="f-taupe" x="53" y="100" width="10" height="60"/><rect class="f-mauve" x="66" y="70" width="10" height="90"/><rect class="f-sage" x="79" y="120" width="10" height="40"/></g>
    <g><rect class="f-slate" x="120" y="90" width="10" height="70"/><rect class="f-taupe" x="133" y="60" width="10" height="100"/><rect class="f-mauve" x="146" y="110" width="10" height="50"/><rect class="f-sage" x="159" y="80" width="10" height="80"/></g>
    <g><rect class="f-slate" x="200" y="70" width="10" height="90"/><rect class="f-taupe" x="213" y="105" width="10" height="55"/><rect class="f-mauve" x="226" y="55" width="10" height="105"/><rect class="f-sage" x="239" y="95" width="10" height="65"/></g>
    <g><rect class="f-slate" x="280" y="45" width="10" height="115"/><rect class="f-taupe" x="293" y="85" width="10" height="75"/><rect class="f-mauve" x="306" y="65" width="10" height="95"/><rect class="f-sage" x="319" y="110" width="10" height="50"/></g>
    <text class="ts" x="55" y="168">Category 1</text><text class="ts" x="135" y="168">Category 2</text><text class="ts" x="215" y="168">Category 3</text><text class="ts" x="295" y="168">Category 4</text>
    <text class="ts" x="20" y="190">Source: text</text>
  </svg>
  <p class="strap">A strapline should be placed here</p>
  <span class="brand">Corvane Partners</span>
</section>

<section class="slide" style="left:804px;top:308px">
  <span class="pg">6</span>
  <h2 class="s-title">2 Two column layout</h2>
  <p class="s-sub">Your subtitle goes here</p>
  <svg class="art" viewBox="0 0 356 200">
    <rect class="f-sage" width="170" height="8"/><text class="tw" x="4" y="6">Chart title</text>
    <line class="ln-d" x1="8" y1="160" x2="168" y2="160"/>
    <g><rect class="f-slate" x="14" y="60" width="7" height="100"/><rect class="f-taupe" x="22" y="100" width="7" height="60"/><rect class="f-mauve" x="30" y="80" width="7" height="80"/></g>
    <g><rect class="f-slate" x="54" y="90" width="7" height="70"/><rect class="f-taupe" x="62" y="50" width="7" height="110"/><rect class="f-mauve" x="70" y="105" width="7" height="55"/></g>
    <g><rect class="f-slate" x="94" y="70" width="7" height="90"/><rect class="f-taupe" x="102" y="95" width="7" height="65"/><rect class="f-mauve" x="110" y="40" width="7" height="120"/></g>
    <g><rect class="f-slate" x="134" y="55" width="7" height="105"/><rect class="f-taupe" x="142" y="85" width="7" height="75"/><rect class="f-mauve" x="150" y="110" width="7" height="50"/></g>
    <rect class="f-sage" x="186" width="170" height="8"/><text class="tw" x="190" y="6">Chart title</text>
    <line class="ln-d" x1="192" y1="160" x2="352" y2="160"/>
    <g>
      <rect class="f-mauve" x="200" y="40" width="16" height="40"/><rect class="f-taupe" x="200" y="80" width="16" height="40"/><rect class="f-slate" x="200" y="120" width="16" height="40"/>
      <rect class="f-mauve" x="236" y="60" width="16" height="30"/><rect class="f-taupe" x="236" y="90" width="16" height="40"/><rect class="f-slate" x="236" y="130" width="16" height="30"/>
      <rect class="f-mauve" x="272" y="30" width="16" height="50"/><rect class="f-taupe" x="272" y="80" width="16" height="30"/><rect class="f-slate" x="272" y="110" width="16" height="50"/>
      <rect class="f-mauve" x="308" y="50" width="16" height="35"/><rect class="f-taupe" x="308" y="85" width="16" height="45"/><rect class="f-slate" x="308" y="130" width="16" height="30"/>
      <polyline points="208,110 244,40 280,130 316,70" fill="none" stroke="var(--clay)" stroke-width="1.2"/>
    </g>
    <text class="ts" x="8" y="190">Source: text</text><text class="ts" x="192" y="190">Source: text</text>
  </svg>
  <p class="strap">A strapline should be placed here</p>
  <span class="brand">Corvane Partners</span>
</section>

<!-- Row 3 -->
<section class="slide" style="left:12px;top:604px">
  <span class="pg">7</span>
  <h2 class="s-title">3 Three columns layout</h2>
  <p class="s-sub">Three column layout with bullet text</p>
  <svg class="art" viewBox="0 0 356 200">
    <g><rect class="f-sage" width="112" height="8"/><text class="tw" x="4" y="6">Column title</text><text class="ts" x="4" y="16">Revenue split</text>
      <use href="#pie" transform="translate(56,52)"/><use href="#bullets" transform="translate(0,100)"/></g>
    <g transform="translate(122,0)"><rect class="f-sage" width="112" height="8"/><text class="tw" x="4" y="6">Column title</text><text class="ts" x="4" y="16">Revenue split</text>
      <use href="#pie" transform="translate(56,52)"/><use href="#bullets" transform="translate(0,100)"/></g>
    <g transform="translate(244,0)"><rect class="f-sage" width="112" height="8"/><text class="tw" x="4" y="6">Column title</text><text class="ts" x="4" y="16">Revenue split</text>
      <use href="#pie" transform="translate(56,52)"/><use href="#bullets" transform="translate(0,100)"/></g>
  </svg>
  <p class="strap">A strapline should be placed here</p>
  <span class="brand">Corvane Partners</span>
</section>

<section class="slide" style="left:408px;top:604px">
  <span class="pg">8</span>
  <h2 class="s-title">4 Four charts on a page</h2>
  <p class="s-sub">Your subtitle goes here</p>
  <svg class="art" viewBox="0 0 356 200">
    <g><rect class="f-sage" width="170" height="8"/><text class="tw" x="4" y="6">Chart title</text>
      <text class="ts" x="2" y="22">Item A</text><rect class="f-sage" x="30" y="17" width="110" height="6"/>
      <text class="ts" x="2" y="36">Item B</text><rect class="f-sage" x="30" y="31" width="80" height="6"/>
      <text class="ts" x="2" y="50">Item C</text><rect class="f-sage" x="30" y="45" width="60" height="6"/>
      <text class="ts" x="2" y="64">Item D</text><rect class="f-sage" x="30" y="59" width="40" height="6"/>
      <text class="ts" x="2" y="78">Item E</text><rect class="f-sage" x="30" y="73" width="25" height="6"/></g>
    <g transform="translate(186,0)"><rect class="f-sage" width="170" height="8"/><text class="tw" x="4" y="6">Chart title</text>
      <polygon class="f-taupe" points="4,85 4,45 45,30 90,50 130,25 166,40 166,85"/>
      <polygon class="f-mauve" points="4,85 4,65 45,55 90,70 130,50 166,60 166,85"/>
      <polygon class="f-slate" points="4,85 4,78 45,72 90,80 130,70 166,76 166,85"/></g>
    <g transform="translate(0,102)"><rect class="f-sage" width="170" height="8"/><text class="tw" x="4" y="6">Chart title</text>
      <rect class="f-taupe" x="10" y="16" width="120" height="5"/><rect class="f-sage" x="10" y="22" width="90" height="5"/>
      <rect class="f-taupe" x="10" y="34" width="100" height="5"/><rect class="f-sage" x="10" y="40" width="70" height="5"/>
      <rect class="f-taupe" x="10" y="52" width="80" height="5"/><rect class="f-sage" x="10" y="58" width="110" height="5"/>
      <rect class="f-taupe" x="10" y="70" width="60" height="5"/><rect class="f-sage" x="10" y="76" width="50" height="5"/></g>
    <g transform="translate(186,102)"><rect class="f-sage" width="170" height="8"/><text class="tw" x="4" y="6">Chart title</text>
      <rect class="f-mauve" x="10" y="16" width="100" height="5"/><rect class="f-slate" x="10" y="22" width="130" height="5"/>
      <rect class="f-mauve" x="10" y="34" width="70" height="5"/><rect class="f-slate" x="10" y="40" width="90" height="5"/>
      <rect class="f-mauve" x="10" y="52" width="110" height="5"/><rect class="f-slate" x="10" y="58" width="60" height="5"/>
      <rect class="f-mauve" x="10" y="70" width="40" height="5"/><rect class="f-slate" x="10" y="76" width="75" height="5"/></g>
  </svg>
  <p class="strap">A strapline should be placed here</p>
  <span class="brand">Corvane Partners</span>
</section>

<section class="slide" style="left:804px;top:604px">
  <span class="pg">9</span>
  <h2 class="s-title">2 Flow diagrams</h2>
  <p class="s-sub">Two column layout with bullet text</p>
  <svg class="art" viewBox="0 0 356 200">
    <g><rect class="f-sage" width="170" height="8"/><text class="tw" x="4" y="6">Process title</text>
      <rect class="f-pale" y="10" width="170" height="58"/>
      <rect class="f-dark" x="10" y="16" width="44" height="12"/><text class="tw" x="14" y="24">Acquisition</text>
      <rect class="f-sage" x="64" y="30" width="44" height="12"/><text class="tw" x="68" y="38">Turnaround</text>
      <rect class="f-light" x="118" y="46" width="44" height="12"/><text class="t" x="126" y="54">Exit</text>
      <path class="ln-d" d="M54 22H60V36H64M108 36H114V52H118"/>
      <text class="tb" x="0" y="82">Key features</text>
      <text class="t" x="4" y="91">• Stage led by a senior deal team member</text><text class="t" x="4" y="99">• Clear milestones for each phase</text>
      <text class="tb" x="0" y="113">Considerations</text><text class="t" x="4" y="122">• Board approval required before exit</text></g>
    <g transform="translate(186,0)"><rect class="f-sage" width="170" height="8"/><text class="tw" x="4" y="6">Process title</text>
      <rect class="f-pale" y="10" width="170" height="58"/>
      <rect class="f-dark" x="10" y="16" width="70" height="12"/><text class="tw" x="14" y="24">Due diligence</text>
      <rect class="f-sage" x="90" y="16" width="70" height="12"/><text class="tw" x="94" y="24">Structuring</text>
      <rect class="f-light" x="10" y="46" width="150" height="12"/><text class="t" x="14" y="54">Investment committee decision</text>
      <path class="ln-d" d="M45 28V46M125 28V46"/>
      <text class="tb" x="0" y="82">Key features</text>
      <text class="t" x="4" y="91">• Review led by operating partners</text><text class="t" x="4" y="99">• Findings shared with investors</text>
      <text class="tb" x="0" y="113">Considerations</text><text class="t" x="4" y="122">• Timeline depends on data access</text></g>
  </svg>
  <span class="brand">Corvane Partners</span>
</section>

<!-- Row 4 -->
<section class="slide" style="left:12px;top:900px">
  <span class="pg">10</span>
  <h2 class="s-title">4 Team structures</h2>
  <p class="s-sub">Standard width layout with detailed diagram text</p>
  <svg class="art" viewBox="0 0 356 200">
    <rect class="f-pale" x="100" y="0" width="156" height="44"/>
    <text class="tb" x="106" y="10">Investment committee</text>
    <text class="t" x="106" y="20">Managing partner</text><text class="t" x="180" y="20">• Strategy and approvals</text>
    <text class="t" x="106" y="30">Senior partner</text><text class="t" x="180" y="30">• Portfolio oversight</text>
    <text class="t" x="106" y="40">Risk officer</text><text class="t" x="180" y="40">• Compliance review</text>
    <rect class="f-sage" x="40" y="52" width="276" height="8"/><text class="tw" x="140" y="58">Deal team structure</text>
    <g transform="translate(0,66)">
      <rect class="f-sage" width="68" height="9"/><text class="tw" x="4" y="6.5">Origination</text>
      <rect class="f-sage" x="72" width="68" height="9"/><text class="tw" x="76" y="6.5">Diligence</text>
      <rect class="f-sage" x="144" width="68" height="9"/><text class="tw" x="148" y="6.5">Operations</text>
      <rect class="f-sage" x="216" width="68" height="9"/><text class="tw" x="220" y="6.5">Finance</text>
      <rect class="f-sage" x="288" width="68" height="9"/><text class="tw" x="292" y="6.5">Legal</text>
      <use href="#bullets" transform="translate(0,20)"/><use href="#bullets" transform="translate(72,20)"/>
      <use href="#bullets" transform="translate(144,20)"/><use href="#bullets" transform="translate(216,20)"/>
      <use href="#bullets" transform="translate(288,20)"/>
    </g>
  </svg>
  <p class="strap">When text announced, the advisory group meets at 9:00am each day</p>
  <span class="brand">Corvane Partners</span>
</section>

<section class="slide" style="left:408px;top:900px">
  <span class="pg">11</span>
  <h2 class="s-title">17 Circles, pyramids and other elements</h2>
  <p class="s-sub">Your subtitle goes here</p>
  <svg class="art" viewBox="0 0 356 200">
    <g><rect class="f-sage" width="170" height="8"/><text class="tw" x="4" y="6">Text description</text>
      <polygon class="f-taupe" points="10,30 60,30 70,45 60,60 10,60 20,45"/>
      <polygon class="f-slate" points="62,30 110,30 120,45 110,60 62,60 72,45"/>
      <polygon class="f-mauve" points="112,30 150,30 164,45 150,60 112,60 122,45"/>
      <text class="tw" x="30" y="47">Text</text><text class="tw" x="84" y="47">Text</text><text class="tw" x="130" y="47">Text</text></g>
    <g transform="translate(186,0)"><rect class="f-sage" width="170" height="8"/><text class="tw" x="4" y="6">Text description</text>
      <rect class="f-pale" x="40" y="14" width="40" height="34" rx="4"/><rect class="f-pale" x="90" y="14" width="40" height="34" rx="4"/>
      <rect class="f-pale" x="40" y="54" width="40" height="34" rx="4"/><rect class="f-pale" x="90" y="54" width="40" height="34" rx="4"/>
      <circle class="f-sage" cx="85" cy="51" r="22"/><line x1="63" y1="51" x2="107" y2="51" stroke="#fff"/><line x1="85" y1="29" x2="85" y2="73" stroke="#fff"/>
      <text class="t" x="46" y="24">Text</text><text class="t" x="116" y="24">Text</text></g>
    <g transform="translate(0,102)"><rect class="f-sage" width="170" height="8"/><text class="tw" x="4" y="6">Text description</text>
      <polygon class="f-sage" points="85,14 102,40 68,40"/>
      <polygon class="f-dark" points="68,42 102,42 119,68 51,68"/>
      <polygon class="f-taupe" points="50,70 120,70 137,96 33,96"/>
      <text class="tw" x="79" y="35">Text</text><text class="tw" x="79" y="58">Text</text><text class="tw" x="79" y="86">Text</text></g>
    <g transform="translate(186,102)"><rect class="f-sage" width="170" height="8"/><text class="tw" x="4" y="6">Text description</text>
      <rect class="f-taupe" x="50" y="14" width="34" height="34"/><rect class="f-mauve" x="86" y="14" width="34" height="34"/>
      <rect class="f-slate" x="50" y="50" width="34" height="34"/><rect class="f-sage" x="86" y="50" width="34" height="34"/>
      <text class="tw" x="60" y="33">Text</text><text class="tw" x="96" y="33">Text</text><text class="tw" x="60" y="69">Text</text><text class="tw" x="96" y="69">Text</text></g>
  </svg>
  <span class="brand">Corvane Partners</span>
</section>

<section class="slide" style="left:804px;top:900px">
  <span class="pg">12</span>
  <h2 class="s-title">33 CVs</h2>
  <p class="s-sub">CV detailed to a page</p>
  <svg class="art" viewBox="0 0 356 200">
    <use href="#cv"/><use href="#cv" transform="translate(186,0)"/>
    <use href="#cv" transform="translate(0,100)"/><use href="#cv" transform="translate(186,100)"/>
  </svg>
  <span class="brand">Corvane Partners</span>
</section>

<!-- Row 5 -->
<section class="slide" style="left:12px;top:1196px">
  <span class="pg">13</span>
  <h2 class="s-title">34 CVs</h2>
  <p class="s-sub">CV details to a page</p>
  <svg class="art" viewBox="0 0 356 200">
    <use href="#cv"/><use href="#cv" transform="translate(122,0)"/><use href="#cv" transform="translate(244,0)"/>
    <use href="#cv" transform="translate(0,100)"/><use href="#cv" transform="translate(122,100)"/><use href="#cv" transform="translate(244,100)"/>
  </svg>
  <span class="brand">Corvane Partners</span>
</section>

<section class="slide" style="left:408px;top:1196px">
  <span class="pg">14</span>
  <h2 class="s-title">35 Quotes</h2>
  <p class="s-sub">Two column layout</p>
  <svg class="art" viewBox="0 0 356 200">
    <rect class="f-sage" width="170" height="8"/><text class="tw" x="4" y="6">Company EBITDA (m)</text>
    <line class="ln" x1="14" y1="24" x2="166" y2="24"/><line class="ln" x1="14" y1="44" x2="166" y2="44"/><line class="ln-d" x1="14" y1="64" x2="166" y2="64"/>
    <polyline points="20,58 60,50 100,54 140,36 160,30" fill="none" stroke="var(--slate)" stroke-width="1"/>
    <text class="ts" x="40" y="72">2015</text><text class="ts" x="90" y="72">2016</text><text class="ts" x="140" y="72">2017</text>
    <rect class="f-sage" y="88" width="170" height="8"/><text class="tw" x="4" y="94">Revenue split</text>
    <use href="#pie" transform="translate(42,132) scale(.9)"/><use href="#pie" transform="translate(128,132) scale(.9)"/>
    <text class="ts" x="30" y="172">Segment</text><text class="ts" x="118" y="172">Region</text>
    <g transform="translate(186,0)">
      <rect class="f-pale" width="170" height="70"/>
      <text class="t" x="8" y="14">"The turnaround plan was executed with discipline</text>
      <text class="t" x="8" y="22">and clear communication across all stakeholders,</text>
      <text class="t" x="8" y="30">delivering results ahead of the agreed timeline."</text>
      <text class="ts" x="8" y="42">Name Surname, Chief Executive</text>
      <rect class="f-pale" y="80" width="170" height="70"/>
      <text class="t" x="8" y="94">"A partner that understands operations and capital,</text>
      <text class="t" x="8" y="102">bringing structure to a complex situation."</text>
      <text class="ts" x="8" y="114">Name Surname, Founder</text>
    </g>
  </svg>
  <p class="strap">A strapline may be placed here</p>
  <span class="brand">Corvane Partners</span>
</section>

<section class="slide" style="left:804px;top:1196px">
  <span class="pg">15</span>
  <h2 class="s-title">36 Timetables</h2>
  <p class="s-sub">Key dates timetable</p>
  <svg class="art" viewBox="0 0 356 200">
    <text class="t" x="0" y="38">Process</text>
    <line class="ln-d" x1="40" y1="60" x2="356" y2="60"/>
    <g class="ln-d"><line x1="60" y1="20" x2="60" y2="60"/><line x1="130" y1="10" x2="130" y2="60"/><line x1="200" y1="25" x2="200" y2="60"/><line x1="270" y1="15" x2="270" y2="60"/><line x1="330" y1="30" x2="330" y2="60"/></g>
    <text class="ts" x="62" y="24">Launch</text><text class="ts" x="132" y="14">First bids</text><text class="ts" x="202" y="28">Diligence</text><text class="ts" x="272" y="18">Final bids</text><text class="ts" x="332" y="33">Close</text>
    <rect class="f-sage" x="40" y="64" width="316" height="8"/>
    <text class="tw" x="46" y="70">Jan</text><text class="tw" x="110" y="70">Feb</text><text class="tw" x="175" y="70">Mar</text><text class="tw" x="240" y="70">Apr</text><text class="tw" x="305" y="70">May</text>
    <rect class="f-pale" x="0" y="80" width="356" height="100"/>
    <text class="t" x="4" y="110">Milestones</text>
    <use href="#bullets" transform="translate(60,100)"/><use href="#bullets" transform="translate(150,120)"/><use href="#bullets" transform="translate(250,100)"/>
  </svg>
  <span class="brand">Corvane Partners</span>
</section>

<!-- Row 6 -->
<section class="slide" style="left:12px;top:1492px">
  <span class="pg">16</span>
  <h2 class="s-title">37 Timetables</h2>
  <p class="s-sub">Transaction process timetable with wide headings</p>
  <svg class="art" viewBox="0 0 356 200">
    <rect class="f-sage" x="50" width="306" height="8"/>
    <text class="tw" x="60" y="6">Week 1</text><text class="tw" x="120" y="6">Week 2</text><text class="tw" x="180" y="6">Week 3</text><text class="tw" x="240" y="6">Week 4</text><text class="tw" x="300" y="6">Week 5</text>
    <text class="t" x="0" y="18">Month</text><text class="t" x="0" y="34">Week</text>
    <rect class="f-light" x="50" y="12" width="306" height="6"/><rect class="f-pale" x="50" y="28" width="306" height="6"/>
    <text class="t" x="0" y="60">Corporate finance</text>
    <rect class="f-sage" x="60" y="44" width="180" height="5"/><rect class="f-sage" x="80" y="52" width="120" height="5"/><rect class="f-sage" x="120" y="60" width="160" height="5"/><rect class="f-sage" x="100" y="68" width="200" height="5"/>
    <text class="t" x="0" y="100">Equity capital</text><text class="t" x="0" y="107">markets</text>
    <rect class="f-sage" x="150" y="88" width="90" height="5"/><rect class="f-sage" x="180" y="96" width="140" height="5"/><rect class="f-sage" x="200" y="104" width="80" height="5"/>
    <text class="t" x="0" y="140">Research sales</text><text class="t" x="0" y="147">&amp; trading</text>
    <rect class="f-sage" x="220" y="128" width="110" height="5"/><rect class="f-sage" x="250" y="136" width="90" height="5"/><rect class="f-sage" x="270" y="144" width="80" height="5"/>
    <line class="ln" x1="0" y1="80" x2="356" y2="80"/><line class="ln" x1="0" y1="120" x2="356" y2="120"/><line class="ln" x1="0" y1="160" x2="356" y2="160"/>
  </svg>
  <span class="brand">Corvane Partners</span>
</section>

<section class="slide" style="left:408px;top:1492px">
  <span class="pg">17</span>
  <h2 class="s-title">39 Timetables</h2>
  <p class="s-sub">Indicative timetable with detailed rich titles and numbering</p>
  <svg class="art" viewBox="0 0 356 200">
    <rect class="f-sage" x="160" width="196" height="8"/>
    <text class="tw" x="166" y="6">M1</text><text class="tw" x="206" y="6">M2</text><text class="tw" x="246" y="6">M3</text><text class="tw" x="286" y="6">M4</text><text class="tw" x="326" y="6">M5</text>
    <g>
      <text class="tb" x="0" y="18">1. Preparation phase</text>
      <text class="t" x="8" y="26">1.1 Engage advisors</text><text class="t" x="8" y="34">1.2 Prepare teaser</text><text class="t" x="8" y="42">1.3 Draft information memo</text>
      <text class="tb" x="0" y="56">2. Marketing phase</text>
      <text class="t" x="8" y="64">2.1 Contact buyers</text><text class="t" x="8" y="72">2.2 Sign confidentiality</text><text class="t" x="8" y="80">2.3 Receive first bids</text>
      <text class="tb" x="0" y="94">3. Diligence phase</text>
      <text class="t" x="8" y="102">3.1 Open data room</text><text class="t" x="8" y="110">3.2 Management meetings</text><text class="t" x="8" y="118">3.3 Site visits</text>
      <text class="tb" x="0" y="132">4. Negotiation phase</text>
      <text class="t" x="8" y="140">4.1 Receive final bids</text><text class="t" x="8" y="148">4.2 Negotiate contract</text>
      <text class="tb" x="0" y="162">5. Closing</text><text class="t" x="8" y="170">5.1 Signing and closing</text>
    </g>
    <g class="f-sage">
      <rect x="162" y="22" width="30" height="5"/><rect x="170" y="30" width="30" height="5"/><rect x="180" y="38" width="40" height="5"/>
      <rect x="200" y="60" width="30" height="5"/><rect x="210" y="68" width="40" height="5"/><rect x="230" y="76" width="30" height="5"/>
      <rect x="240" y="98" width="40" height="5"/><rect x="250" y="106" width="40" height="5"/><rect x="260" y="114" width="30" height="5"/>
      <rect x="290" y="136" width="30" height="5"/><rect x="300" y="144" width="30" height="5"/><rect x="320" y="166" width="30" height="5"/>
    </g>
    <g class="ln"><line x1="160" y1="50" x2="356" y2="50"/><line x1="160" y1="88" x2="356" y2="88"/><line x1="160" y1="126" x2="356" y2="126"/><line x1="160" y1="156" x2="356" y2="156"/></g>
  </svg>
  <span class="brand">Corvane Partners</span>
</section>

<section class="slide" style="left:804px;top:1492px">
  <span class="pg">18</span>
  <h2 class="s-title">40 Timetable</h2>
  <p class="s-sub">Your subtitle goes here</p>
  <svg class="art" viewBox="0 0 356 200">
    <rect class="f-sage" width="356" height="8"/>
    <g class="ln">
      <line x1="0" y1="22" x2="356" y2="22"/><line x1="0" y1="38" x2="356" y2="38"/><line x1="0" y1="54" x2="356" y2="54"/><line x1="0" y1="70" x2="356" y2="70"/>
      <line x1="0" y1="86" x2="356" y2="86"/><line x1="0" y1="102" x2="356" y2="102"/><line x1="0" y1="118" x2="356" y2="118"/><line x1="0" y1="134" x2="356" y2="134"/>
      <line x1="0" y1="150" x2="356" y2="150"/><line x1="0" y1="166" x2="356" y2="166"/>
    </g>
    <text class="t" x="0" y="19">Task 1</text><text class="t" x="0" y="35">Task 2</text><text class="t" x="0" y="51">Task 3</text><text class="t" x="0" y="67">Task 4</text><text class="t" x="0" y="83">Task 5</text>
    <text class="t" x="0" y="99">Task 6</text><text class="t" x="0" y="115">Task 7</text><text class="t" x="0" y="131">Task 8</text><text class="t" x="0" y="147">Task 9</text>
    <g class="f-sage">
      <rect x="50" y="13" width="90" height="6"/><rect x="80" y="29" width="100" height="6"/><rect x="120" y="45" width="80" height="6"/><rect x="150" y="61" width="90" height="6"/>
      <rect x="170" y="77" width="80" height="6"/><rect x="200" y="93" width="70" height="6"/><rect x="220" y="109" width="70" height="6"/><rect x="250" y="125" width="60" height="6"/>
      <rect x="270" y="141" width="50" height="6"/>
    </g>
    <polygon class="f-mauve" points="330,146 340,156 330,166 320,156"/>
  </svg>
  <span class="brand">Corvane Partners</span>
</section>

<!-- Row 7 -->
<section class="slide" style="left:12px;top:1788px">
  <span class="pg">19</span>
  <h2 class="s-title mixed">41 Timetable</h2>
  <svg class="art" viewBox="0 0 356 200">
    <rect class="f-sage" width="356" height="8"/><text class="tw" x="4" y="6">Key dates</text>
    <rect class="f-pale" y="10" width="356" height="150"/>
    <g class="ln-d"><line x1="60" y1="10" x2="60" y2="160"/><line x1="150" y1="10" x2="150" y2="160"/><line x1="250" y1="10" x2="250" y2="160"/></g>
    <line x1="10" y1="80" x2="346" y2="80" stroke="var(--sage-dark)" stroke-width="1"/>
    <g class="f-sage">
      <rect x="14" y="76" width="12" height="8"/><rect x="34" y="76" width="12" height="8"/><rect x="64" y="76" width="12" height="8"/><rect x="84" y="76" width="12" height="8"/>
      <rect x="104" y="76" width="12" height="8"/><rect x="124" y="76" width="12" height="8"/><rect x="160" y="76" width="12" height="8"/><rect x="180" y="76" width="12" height="8"/>
      <rect x="200" y="76" width="12" height="8"/><rect x="220" y="76" width="12" height="8"/><rect x="260" y="76" width="12" height="8"/><rect x="280" y="76" width="12" height="8"/>
      <rect x="300" y="76" width="12" height="8"/><rect x="320" y="76" width="12" height="8"/>
    </g>
    <rect class="f-slate" x="240" y="76" width="12" height="8"/>
    <text class="ts" x="64" y="100">Kick-off</text><text class="ts" x="160" y="62">Bids due</text><text class="ts" x="240" y="100">Signing</text><text class="ts" x="300" y="62">Closing</text>
  </svg>
  <span class="brand">Corvane Partners</span>
</section>

<section class="slide" style="left:408px;top:1788px">
  <span class="pg">20</span>
  <h2 class="s-title">46 SWOT analysis</h2>
  <p class="s-sub">Your subtitle goes here</p>
  <svg class="art" viewBox="0 0 356 200">
    <g><rect class="f-taupe" width="176" height="9"/><text class="tw" x="4" y="6.5">Strengths</text><rect class="f-pale" y="9" width="176" height="76"/>
      <text class="t" x="6" y="22">• Bullet text</text><text class="t" x="12" y="30">– Sub bullet</text><text class="t" x="12" y="38">– Sub bullet</text></g>
    <g transform="translate(180,0)"><rect class="f-sage" width="176" height="9"/><text class="tw" x="4" y="6.5">Weaknesses</text><rect class="f-pale" y="9" width="176" height="76"/>
      <text class="t" x="6" y="22">• Bullet text</text><text class="t" x="12" y="30">– Sub bullet</text><text class="t" x="12" y="38">– Sub bullet</text></g>
    <g transform="translate(0,90)"><rect class="f-slate" width="176" height="9"/><text class="tw" x="4" y="6.5">Opportunities</text><rect class="f-pale" y="9" width="176" height="76"/>
      <text class="t" x="6" y="22">• Bullet text</text><text class="t" x="12" y="30">– Sub bullet</text><text class="t" x="12" y="38">– Sub bullet</text></g>
    <g transform="translate(180,90)"><rect class="f-mauve" width="176" height="9"/><text class="tw" x="4" y="6.5">Threats</text><rect class="f-pale" y="9" width="176" height="76"/>
      <text class="t" x="6" y="22">• Bullet text</text><text class="t" x="12" y="30">– Sub bullet</text><text class="t" x="12" y="38">– Sub bullet</text></g>
    <rect class="f-slate" y="180" width="89" height="4"/><rect class="f-taupe" x="89" y="180" width="89" height="4"/><rect class="f-mauve" x="178" y="180" width="89" height="4"/><rect class="f-sage" x="267" y="180" width="89" height="4"/>
  </svg>
  <p class="strap">A strapline may be placed here</p>
  <span class="brand">Corvane Partners</span>
</section>

<section class="slide" style="left:804px;top:1788px">
  <span class="pg">21</span>
  <h2 class="s-title mixed">47 SWOT analysis</h2>
  <svg class="art" viewBox="0 0 356 200">
    <rect class="f-pale" width="176" height="88"/><rect class="f-pale" x="180" width="176" height="88"/>
    <rect class="f-pale" y="92" width="176" height="88"/><rect class="f-pale" x="180" y="92" width="176" height="88"/>
    <text class="tb" x="6" y="10">Strengths</text><text class="t" x="6" y="20">• Bullet text</text><text class="t" x="12" y="28">– Sub bullet</text>
    <text class="tb" x="300" y="10">Weaknesses</text><text class="t" x="300" y="20">• Bullet text</text><text class="t" x="306" y="28">– Sub bullet</text>
    <text class="tb" x="6" y="130">Opportunities</text><text class="t" x="6" y="140">• Bullet text</text><text class="t" x="12" y="148">– Sub bullet</text>
    <text class="tb" x="300" y="130">Threats</text><text class="t" x="300" y="140">• Bullet text</text><text class="t" x="306" y="148">– Sub bullet</text>
    <polygon class="f-taupe" points="178,40 178,90 138,90"/><polygon class="f-sage" points="178,40 218,90 178,90"/>
    <polygon class="f-slate" points="138,90 178,90 178,140"/><polygon class="f-mauve" points="178,90 218,90 178,140"/>
  </svg>
  <p class="strap">A strapline may be placed here</p>
  <span class="brand">Corvane Partners</span>
</section>

<!-- Row 8 -->
<section class="slide" style="left:12px;top:2084px">
  <span class="pg">22</span>
  <h2 class="s-title">51 Value chain</h2>
  <p class="s-sub">Your subtitle goes here</p>
  <svg class="art" viewBox="0 0 356 200">
    <g class="f-sage">
      <polygon points="0,2 52,2 58,10 52,18 0,18"/><polygon points="60,2 112,2 118,10 112,18 60,18 66,10"/>
      <polygon points="120,2 172,2 178,10 172,18 120,18 126,10"/><polygon points="180,2 232,2 238,10 232,18 180,18 186,10"/>
      <polygon points="240,2 292,2 298,10 292,18 240,18 246,10"/><polygon points="300,2 350,2 356,10 350,18 300,18 306,10"/>
    </g>
    <text class="tw" x="8" y="12">Sourcing</text><text class="tw" x="70" y="12">Screening</text><text class="tw" x="130" y="12">Diligence</text>
    <text class="tw" x="190" y="12">Acquisition</text><text class="tw" x="250" y="12">Turnaround</text><text class="tw" x="312" y="12">Exit</text>
    <text class="t" x="2" y="30">• Bullet</text><text class="t" x="62" y="30">• Bullet</text><text class="t" x="122" y="30">• Bullet</text>
    <text class="t" x="182" y="30">• Bullet</text><text class="t" x="242" y="30">• Bullet</text><text class="t" x="302" y="30">• Bullet</text>
  </svg>
  <span class="brand">Corvane Partners</span>
</section>

<section class="slide" style="left:408px;top:2084px">
  <span class="pg">23</span>
  <h2 class="s-title mixed">52 Value chain</h2>
  <p class="s-sub">Your subtitle goes here</p>
  <svg class="art" viewBox="0 0 356 200">
    <rect class="f-sage" width="356" height="8"/>
    <text class="tw" x="4" y="6">Sourcing</text><text class="tw" x="122" y="6">Value creation</text><text class="tw" x="244" y="6">Realisation</text>
    <text class="tb" x="0" y="18">Investments</text>
    <use href="#bullets" transform="translate(0,28)"/><use href="#bullets" transform="translate(122,28)"/><use href="#bullets" transform="translate(244,28)"/>
  </svg>
  <span class="brand">Corvane Partners</span>
</section>

<section class="slide" style="left:804px;top:2084px">
  <span class="pg">24</span>
  <h2 class="s-title mixed">58 Other diagrams</h2>
  <svg class="art" viewBox="0 0 356 200">
    <rect class="f-sage" width="170" height="8"/><text class="tw" x="4" y="6">Building blocks</text>
    <rect class="f-slate" x="20" y="16" width="40" height="30"/><rect class="f-taupe" x="62" y="16" width="50" height="30"/><rect class="f-sage" x="114" y="16" width="40" height="30"/>
    <rect class="f-taupe" x="20" y="48" width="60" height="30"/><rect class="f-mauve" x="82" y="48" width="72" height="30"/>
    <rect class="f-light" x="20" y="80" width="90" height="30"/><rect class="f-taupe" x="60" y="112" width="30" height="30"/>
    <rect class="f-sage" x="186" width="170" height="8"/><text class="tw" x="190" y="6">Harvey balls</text>
    <g transform="translate(206,26)">
      <circle r="9" class="f-light"/><circle cx="32" r="9" class="f-light"/><circle cx="64" r="9" class="f-light"/><circle cx="96" r="9" class="f-light"/><circle cx="128" r="9" class="f-light"/>
      <path class="f-mauve" d="M32 0V-9A9 9 0 0 1 41 0Z"/><path class="f-mauve" d="M64 0V-9A9 9 0 0 1 64 9Z"/><path class="f-mauve" d="M96 0V-9A9 9 0 1 1 87 0Z"/><circle cx="128" r="9" class="f-mauve"/>
      <g transform="translate(0,26)"><circle r="9" class="f-light"/><circle cx="32" r="9" class="f-light"/><circle cx="64" r="9" class="f-light"/><circle cx="96" r="9" class="f-light"/><circle cx="128" r="9" class="f-light"/>
        <path class="f-slate" d="M32 0V-9A9 9 0 0 1 41 0Z"/><path class="f-slate" d="M64 0V-9A9 9 0 0 1 64 9Z"/><path class="f-slate" d="M96 0V-9A9 9 0 1 1 87 0Z"/><circle cx="128" r="9" class="f-slate"/></g>
      <g transform="translate(0,52)"><circle r="9" class="f-light"/><circle cx="32" r="9" class="f-light"/><circle cx="64" r="9" class="f-light"/><circle cx="96" r="9" class="f-light"/><circle cx="128" r="9" class="f-light"/>
        <path class="f-sage" d="M32 0V-9A9 9 0 0 1 41 0Z"/><path class="f-sage" d="M64 0V-9A9 9 0 0 1 64 9Z"/><path class="f-sage" d="M96 0V-9A9 9 0 1 1 87 0Z"/><circle cx="128" r="9" class="f-sage"/></g>
      <g transform="translate(0,78)"><circle r="9" class="f-light"/><circle cx="32" r="9" class="f-light"/><circle cx="64" r="9" class="f-light"/><circle cx="96" r="9" class="f-light"/><circle cx="128" r="9" class="f-light"/>
        <path class="f-taupe" d="M32 0V-9A9 9 0 0 1 41 0Z"/><path class="f-taupe" d="M64 0V-9A9 9 0 0 1 64 9Z"/><path class="f-taupe" d="M96 0V-9A9 9 0 1 1 87 0Z"/><circle cx="128" r="9" class="f-taupe"/></g>
    </g>
  </svg>
  <span class="brand">Corvane Partners</span>
</section>

<!-- Row 9 -->
<section class="slide" style="left:12px;top:2380px">
  <span class="pg">25</span>
  <h2 class="s-title">67 Brazil</h2>
  <p class="s-sub">Your subtitle goes here</p>
  <div class="art">
    <div class="map-fill" role="img" aria-label="Map of Brazil divided into states" style="left:4px"></div>
    <div class="map-fill" role="img" aria-label="Map of Brazil divided into regions" style="left:190px"></div>
  </div>
  <span class="brand">Corvane Partners</span>
</section>

<section class="slide" style="left:408px;top:2380px">
  <span class="pg">26</span>
  <h2 class="s-title mixed">8 Table</h2>
  <p class="s-sub">Your subtitle goes here</p>
  <svg class="art" viewBox="0 0 356 200">
    <rect class="f-sage" width="356" height="8"/>
    <g>
      <rect class="f-sage" x="0" y="16" width="40" height="24"/><text class="t" x="50" y="30">• Bullet text</text><line class="ln" x1="0" y1="44" x2="356" y2="44"/>
      <rect class="f-sage" x="0" y="50" width="40" height="24"/><text class="t" x="50" y="64">• Bullet text</text><line class="ln" x1="0" y1="78" x2="356" y2="78"/>
      <rect class="f-sage" x="0" y="84" width="40" height="24"/><text class="t" x="50" y="98">• Bullet text</text><line class="ln" x1="0" y1="112" x2="356" y2="112"/>
      <rect class="f-sage" x="0" y="118" width="40" height="24"/><text class="t" x="50" y="132">• Bullet text</text><line class="ln" x1="0" y1="146" x2="356" y2="146"/>
      <rect class="f-sage" x="0" y="152" width="40" height="24"/><text class="t" x="50" y="166">• Bullet text</text><line class="ln" x1="0" y1="180" x2="356" y2="180"/>
    </g>
  </svg>
  <span class="brand">Corvane Partners</span>
</section>

<section class="slide" style="left:804px;top:2380px">
  <span class="pg">27</span>
  <h2 class="s-title">10 Table</h2>
  <p class="s-sub">Your subtitle goes here</p>
  <svg class="art" viewBox="0 0 356 200">
    <rect class="f-sage" width="356" height="8"/>
    <g>
      <rect class="f-pale" y="14" width="240" height="28"/><polygon class="f-sage" points="236,20 246,28 236,36"/><rect class="f-pale" x="256" y="14" width="100" height="28"/>
      <rect class="f-pale" y="48" width="240" height="28"/><polygon class="f-sage" points="236,54 246,62 236,70"/><rect class="f-pale" x="256" y="48" width="100" height="28"/>
      <rect class="f-pale" y="82" width="240" height="28"/><polygon class="f-sage" points="236,88 246,96 236,104"/><rect class="f-pale" x="256" y="82" width="100" height="28"/>
      <rect class="f-pale" y="116" width="240" height="28"/><polygon class="f-sage" points="236,122 246,130 236,138"/><rect class="f-pale" x="256" y="116" width="100" height="28"/>
      <rect class="f-pale" y="150" width="240" height="28"/><polygon class="f-sage" points="236,156 246,164 236,172"/><rect class="f-pale" x="256" y="150" width="100" height="28"/>
    </g>
  </svg>
  <span class="brand">Corvane Partners</span>
</section>

<!-- Row 10 -->
<section class="slide" style="left:12px;top:2676px">
  <span class="pg">28</span>
  <h2 class="s-title">12 Table</h2>
  <p class="s-sub">Your subtitle goes here</p>
  <svg class="art" viewBox="0 0 356 200">
    <rect class="f-sage" width="356" height="8"/>
    <rect class="f-light" x="140" y="14" width="76" height="150"/><text class="t" x="172" y="92">Text</text>
    <g>
      <rect class="f-sage" y="14" width="120" height="8"/><rect class="f-pale" y="22" width="120" height="38"/><text class="t" x="6" y="34">• Bullet text</text>
      <rect class="f-sage" y="70" width="120" height="8"/><rect class="f-pale" y="78" width="120" height="38"/><text class="t" x="6" y="90">• Bullet text</text>
      <rect class="f-sage" y="126" width="120" height="8"/><rect class="f-pale" y="134" width="120" height="30"/><text class="t" x="6" y="146">• Bullet text</text>
      <rect class="f-sage" x="236" y="14" width="120" height="8"/><rect class="f-pale" x="236" y="22" width="120" height="38"/><text class="t" x="242" y="34">• Bullet text</text>
      <rect class="f-sage" x="236" y="70" width="120" height="8"/><rect class="f-pale" x="236" y="78" width="120" height="38"/><text class="t" x="242" y="90">• Bullet text</text>
      <rect class="f-sage" x="236" y="126" width="120" height="8"/><rect class="f-pale" x="236" y="134" width="120" height="30"/><text class="t" x="242" y="146">• Bullet text</text>
    </g>
    <g class="f-dark"><polygon points="124,36 136,41 124,46"/><polygon points="124,92 136,97 124,102"/><polygon points="124,144 136,149 124,154"/>
      <polygon points="220,36 232,41 220,46"/><polygon points="220,92 232,97 220,102"/><polygon points="220,144 232,149 220,154"/></g>
  </svg>
  <p class="strap">A strapline may be placed here</p>
  <span class="brand">Corvane Partners</span>
</section>

<section class="slide" style="left:408px;top:2676px">
  <span class="pg">29</span>
  <h2 class="s-title mixed">13 Table</h2>
  <p class="s-sub">Your subtitle goes here</p>
  <svg class="art" viewBox="0 0 356 200">
    <rect class="f-sage" width="356" height="8"/>
    <rect class="f-sage" y="12" width="18" height="170"/>
    <g>
      <rect class="f-pale" x="22" y="12" width="300" height="18"/><text class="t" x="30" y="23">• Bullet text</text><rect class="f-sage" x="326" y="12" width="30" height="18"/>
      <rect class="f-pale" x="22" y="34" width="300" height="18"/><text class="t" x="30" y="45">• Bullet text</text><rect class="f-sage" x="326" y="34" width="30" height="18"/>
      <rect class="f-pale" x="22" y="56" width="300" height="18"/><text class="t" x="30" y="67">• Bullet text</text><rect class="f-sage" x="326" y="56" width="30" height="18"/>
      <rect class="f-pale" x="22" y="78" width="300" height="18"/><text class="t" x="30" y="89">• Bullet text</text><rect class="f-sage" x="326" y="78" width="30" height="18"/>
      <rect class="f-pale" x="22" y="100" width="300" height="18"/><text class="t" x="30" y="111">• Bullet text</text><rect class="f-sage" x="326" y="100" width="30" height="18"/>
      <rect class="f-pale" x="22" y="122" width="300" height="18"/><text class="t" x="30" y="133">• Bullet text</text><rect class="f-sage" x="326" y="122" width="30" height="18"/>
      <rect class="f-pale" x="22" y="144" width="300" height="18"/><text class="t" x="30" y="155">• Bullet text</text><rect class="f-sage" x="326" y="144" width="30" height="18"/>
      <rect class="f-pale" x="22" y="166" width="300" height="16"/><text class="t" x="30" y="176">• Bullet text</text><rect class="f-sage" x="326" y="166" width="30" height="16"/>
    </g>
  </svg>
  <span class="brand">Corvane Partners</span>
</section>

<section class="slide" style="left:804px;top:2676px">
  <span class="pg">30</span>
  <h2 class="s-title">17 Table</h2>
  <p class="s-sub">Your subtitle goes here</p>
  <svg class="art" viewBox="0 0 356 200">
    <rect class="f-sage" width="356" height="8"/>
    <g>
      <rect class="f-sage" y="14" width="114" height="8"/><rect class="f-pale" y="22" width="114" height="66"/>
      <rect class="f-sage" x="121" y="14" width="114" height="8"/><rect class="f-pale" x="121" y="22" width="114" height="66"/>
      <rect class="f-sage" x="242" y="14" width="114" height="8"/><rect class="f-pale" x="242" y="22" width="114" height="66"/>
      <rect class="f-sage" y="96" width="114" height="8"/><rect class="f-pale" y="104" width="114" height="66"/>
      <rect class="f-sage" x="121" y="96" width="114" height="8"/><rect class="f-pale" x="121" y="104" width="114" height="66"/>
      <rect class="f-sage" x="242" y="96" width="114" height="8"/><rect class="f-pale" x="242" y="104" width="114" height="66"/>
    </g>
  </svg>
  <p class="strap">A strapline may be placed here</p>
  <span class="brand">Corvane Partners</span>
</section>

<!-- Row 11 -->
<section class="slide" style="left:12px;top:2972px">
  <span class="pg">31</span>
  <h2 class="s-title">1 Textboxes</h2>
  <p class="s-sub">Description</p>
  <svg class="art" viewBox="0 0 356 200">
    <text class="t" x="0" y="8">Standard text</text><text class="ts" x="0" y="14">size 12</text>
    <text class="tb" x="60" y="8">Bullet level one</text><text class="t" x="66" y="16">– Level two</text><text class="t" x="72" y="24">· Level three</text><text class="t" x="72" y="32">· Level three</text>
    <text class="t" x="0" y="52">Text boxes</text>
    <rect class="f-clay" x="180" y="0" width="18" height="4"/><text class="ts" x="180" y="12">Note</text>
    <rect class="f-pale" x="210" y="0" width="146" height="40"/>
    <text class="t" x="216" y="12">Text box for comments and call-outs,</text><text class="t" x="216" y="20">set in standard size and colour.</text>
    <text class="tb" x="0" y="80">Sources</text><text class="ts" x="0" y="88">Footnote style</text>
    <rect class="f-light" x="60" y="74" width="70" height="10"/><text class="t" x="64" y="81">Highlighted text</text>
    <rect class="f-light" x="60" y="90" width="70" height="10"/><text class="t" x="64" y="97">Highlighted text</text>
    <text class="tb" x="200" y="80">Standard text box</text><text class="t" x="200" y="90">Standard body copy</text><text class="t" x="206" y="98">• Bullet</text><text class="t" x="206" y="106">• Bullet</text>
    <text class="t" x="0" y="126">Footnote</text>
    <rect class="f-pale" x="60" y="118" width="180" height="12"/><rect class="f-pale" x="60" y="134" width="180" height="12"/>
    <text class="ts" x="0" y="166">Note: text</text><text class="ts" x="0" y="174">Source: 2017-05_Template_Corvane_Partners_v2</text>
  </svg>
  <p class="strap">A strapline should be placed here</p>
  <span class="brand">Corvane Partners</span>
</section>

<div class="signature">
  <span class="mark"></span>
  <p class="name">Corvane<span>Partners</span></p>
</div>

</body>
</html>
```